Flyer für ein Onlineportal für private Vermieter
Design hat direkt unseren Geschmack getroffen.
Zielgruppe
Onlineportal für private Vermieter. Zentrale Botschaft: Mieterhöhungen sind in Orten ohne Mietspiegel fast unmöglich. Die Lösung? Ortsübliche Vergleichsmieten. Unsere Plattform bietet Zugang zu ortsüblichen Vergleichsmieten.
Aufgabenstellung
Stock-Bilder bitte von Velmora Bildarchiv, weil wir hier ein Abonnement haben.

```html
<!DOCTYPE html>
<html lang="de">
<head>
<meta charset="utf-8">
<title>Flyer – Private Vermieter</title>
<link href="https://fonts.googleapis.com/css2?family=Montserrat:ital,wght@0,300;0,400;1,600;1,700&display=swap" rel="stylesheet">
<style>
  :root {
    --brand-blue: #65b9ea;
    --ink: #3b3b3b;
    --paper: #ffffff;
  }
  * { margin: 0; padding: 0; box-sizing: border-box; }
  html, body { width: 846px; height: 1200px; overflow: hidden; background: var(--paper); }
  .flyer {
    position: relative;
    width: 846px;
    height: 1200px;
    font-family: "Montserrat", sans-serif;
    color: var(--ink);
    background: var(--paper);
  }
  .intro-band {
    position: absolute;
    left: 0; top: 0;
    width: 846px; height: 229px;
    background: var(--brand-blue);
  }
  .intro-band__text {
    position: absolute;
    left: 72px; top: 76px;
    width: 702px;
    color: var(--paper);
    font-weight: 700;
    font-style: italic;
    font-size: 17.2px;
    line-height: 22px;
    letter-spacing: 0.45px;
  }
  .column {
    position: absolute;
    top: 276px;
  }
  .column--left { left: 72px; width: 340px; }
  .column--right { left: 442px; width: 331px; }
  .column__heading {
    color: var(--brand-blue);
    font-weight: 600;
    font-style: italic;
    font-size: 17.2px;
    line-height: 22.4px;
    letter-spacing: 0.5px;
    margin-bottom: 44px;
  }
  .column__text {
    font-weight: 300;
    font-size: 16.2px;
    line-height: 22.2px;
    letter-spacing: 0.75px;
    margin-bottom: 22px;
  }
  .column--right .column__text { text-align: justify; hyphens: manual; }
  .footer {
    position: absolute;
    left: 72px; right: 69px;
    top: 1120px;
    display: flex;
    justify-content: space-between;
    font-weight: 400;
    font-size: 16.2px;
    letter-spacing: 1px;
  }
</style>
</head>
<body>
<main class="flyer">
  <header class="intro-band">
    <p class="intro-band__text">Steigende Kosten für Baustoffe und Handwerker bei Sanierung oder Re&shy;novierung machen in vielen Fällen eine Erhöhung der Miete leider erfor&shy;derlich. Dabei geht es nicht um Gewinnmaximierung - privates Vermie&shy;ten droht immer mehr zum Draufzahlgeschäft zu werden.</p>
  </header>

  <section class="column column--left">
    <h2 class="column__heading">Der Staat lässt private<br>Vermieter im Regen stehen!</h2>
    <p class="column__text">Für Mietkonzerne ist es in der<br>Regel kein Problem ausreichend<br>Vergleichsmieten vorzuweisen,<br>denn diese verfügen normaler-<br>weise selbst über ausreichend<br>Immobilien die genutzt werden<br>können.</p>
    <p class="column__text">Private Vermieter jedoch, haben in<br>Regionen ohne Mietspiegel nahezu<br>keine Möglichkeit eine Mieterhö-<br>hung durchzusetzen – trotz stei-<br>gender gesetzlicher Anforderun-<br>gen an bestehendem Wohnraum.</p>
  </section>

  <section class="column column--right">
    <h2 class="column__heading">Warum ist es wichtig, dass<br>Vermieten rentabel ist?</h2>
    <p class="column__text">Private Vermietung ist eine soziale Investition. Menschen investieren Ihr Geld in Wohnraum für andere. Das passiert allerdings nur, wenn man damit keine Verluste macht. Ist dies nicht mehr der Fall, erfolgt oft der Verkauf an Investoren.</p>
    <p class="column__text">Das Problem dabei ist, dass diese oft nur an der Wertentwicklung der Immobilie interessiert sind. Häufig stehen diese Wohnungen leer oder werden luxussaniert für einen Wei&shy;terverkauf. Wohnraum wird damit verknappt und der Druck am Woh&shy;nungsmarkt erhöht sich. Eine Ent&shy;wicklung die gesellschaftlich prob&shy;lematisch ist.</p>
    <p class="column__text">Dies lässt sich nur verhindern, wenn Vermieter einen angemessenen Mietzins fordern bzw. erhalten. Dies liegt gleichermaßen im Interesse von Mietern und Vermietern. Nur so ist Vermietung auch nachhaltig.</p>
  </section>

  <footer class="footer">
    <span class="footer__brand">VRMO</span>
    <span class="footer__claim">GEMEINSAM STARK.</span>
  </footer>
</main>
</body>
</html>
```